Business Card Project for Firm Deck Hoisting

Business name is "Firm Deck Hoisting" we are a scaffolding & rigging business specialising in local and remote work for:
- scaffolding (residential, commercial, industrial)
- rigging
-man material hoists
- swing stages
- labour hire

On the back of the card I would like FDH as the symbol / logo. I have attached the logos we have had created by sketch harbour. We would like to use bold colours – preferably as the same colour scheme as the logo.

Target Market(s)

Construction business

Industry/Entity Type

Construction

Contact Information for Business Card

name: Owen Pellew
Title: Director
Phone: 0491 572 864
Address: PO BOX 3251, Elmsvale SA 5174
Email: owen@firmdeckhoisting.com.au
Website: www.firmdeckhoisting.com.au

Font styles to use
Sans Serif

Requirements
Must have
• Must use existing logo & prefering using bold colours
Nice to have
• Would be nice to have a line of dot points in what we specialise in but not essential
• Would be nice to see some designs with a slogan but not essential
Should not have
• NA

```html
<!DOCTYPE html>
<html lang="en">
<head>
<meta charset="utf-8">
<title>Firm Deck Hoisting – Business Card</title>
<link href="https://fonts.googleapis.com/css2?family=Michroma&family=Open+Sans:wght@400&display=swap" rel="stylesheet">
<style>
  :root {
    --stage: #000000;
    --card-light: #f2f2f2;
    --ink: #1d1d1f;
    --brand-blue: #1a6fc0;
    --blue-top: #3f97dd;
    --blue-bottom: #0a579d;
    --white: #ffffff;
  }
  * { margin: 0; padding: 0; box-sizing: border-box; }
  html, body {
    width: 1200px; height: 900px; overflow: hidden;
    background: var(--stage);
  }
  .canvas { position: relative; width: 1200px; height: 900px; }

  .card {
    position: absolute; top: 200px; width: 310px; height: 502px;
  }
  .card-front {
    left: 292px;
    background: var(--card-light);
    border-radius: 62px 0 62px 0;
    color: var(--ink);
  }
  .card-back {
    left: 641px; width: 309px;
    background: linear-gradient(150deg, var(--blue-top) 0%, #1f72bb 45%, var(--blue-bottom) 100%);
    border-radius: 0 62px 0 62px;
    color: var(--white);
  }

  .wordmark {
    position: absolute; left: 0; right: 0; top: 118px;
    display: flex; align-items: center; justify-content: center; gap: 10px;
    font-family: "Michroma", sans-serif;
    font-size: 15px; line-height: 1.35; letter-spacing: 1px;
    text-align: left;
  }
  .wordmark-square { width: 34px; height: 34px; flex: none; }
  .card-front .wordmark { color: var(--ink); }
  .card-front .wordmark-square { background: var(--brand-blue); }
  .card-back .wordmark { color: var(--white); }
  .card-back .wordmark-square { background: var(--white); }

  .person { position: absolute; left: 26px; top: 211px; font-family: "Michroma", sans-serif; }
  .person-name { font-size: 15px; letter-spacing: 0.5px; }
  .person-name .surname { color: var(--brand-blue); }
  .person-title { font-size: 11.5px; margin-top: 4px; letter-spacing: 0.3px; }

  .contact-list {
    position: absolute; left: 26px; top: 301px; list-style: none;
    font-family: "Open Sans", sans-serif; font-size: 14.5px; line-height: 19.5px;
  }
  .contact-list li { display: flex; align-items: center; gap: 7px; }
  .contact-icon { width: 10px; height: 10px; flex: none; }

  .postal {
    position: absolute; left: 26px; top: 404px;
    font-family: "Michroma", sans-serif; font-size: 10px; letter-spacing: 0.1px;
  }

  .services {
    position: absolute; left: 0; right: 0; top: 244px; list-style: none;
    text-align: center;
    font-family: "Michroma", sans-serif; font-size: 15px; line-height: 30px; letter-spacing: 0.6px;
  }
</style>
</head>
<body>
<main class="canvas">
  <section class="card card-front" aria-label="Card front">
    <div class="wordmark">
      <span class="wordmark-square"></span>
      <span>FIRM DECK<br>HOISTING</span>
    </div>
    <div class="person">
      <p class="person-name">OWEN <span class="surname">PELLEW</span></p>
      <p class="person-title">DIRECTOR</p>
    </div>
    <ul class="contact-list">
      <li>
        <svg class="contact-icon" viewBox="0 0 10 10" aria-hidden="true"><rect x="2.5" y="0.5" width="5" height="9" rx="1" fill="none" stroke="#1a6fc0" stroke-width="1.2"/><circle cx="5" cy="8" r="0.6" fill="#1a6fc0"/></svg>
        <span>0491 572 864</span>
      </li>
      <li>
        <svg class="contact-icon" viewBox="0 0 10 10" aria-hidden="true"><rect x="0.5" y="2" width="9" height="6.5" fill="#1a6fc0"/><path d="M0.5 2 L5 5.5 L9.5 2" fill="none" stroke="#f2f2f2" stroke-width="0.9"/></svg>
        <span>owen@firmdeckhoisting.com.au</span>
      </li>
      <li>
        <svg class="contact-icon" viewBox="0 0 10 10" aria-hidden="true"><circle cx="5" cy="5" r="4.5" fill="#1a6fc0"/><path d="M2.5 3.5 Q4 3 4.5 5 Q5 7 6.5 7.5 M6 2 Q7.5 3 7 4.5" fill="none" stroke="#f2f2f2" stroke-width="0.8"/></svg>
        <span>www.firmdeckhoisting.com.au</span>
      </li>
    </ul>
    <p class="postal">PO BOX 3251, ELMSVALE SA 5174</p>
  </section>

  <section class="card card-back" aria-label="Card back">
    <div class="wordmark">
      <span class="wordmark-square"></span>
      <span>FIRM DECK<br>HOISTING</span>
    </div>
    <ul class="services">
      <li>SCAFFOLDING</li>
      <li>RIGGING</li>
      <li>MAN MATERIAL HOISTS</li>
      <li>SWING STAGES</li>
      <li>LABOUR HIRE</li>
    </ul>
  </section>
</main>
</body>
</html>
```